Business Card Design Project

We need a Business Card for an Mechanical Engineering firm in Singapore. The design should be Modern & Technical looking, yet eye catching.

Our company deals in Cutting Tools & Machine Accessories for the Manufacturing Industries such as Oil & Gas, Aero Space, etc... For more information on our Company, you can either email me or view our website www.valtrion.com.sg.

We are trying to revamp our image to give our consumers a fresh new perspective to our company, so we welcome all ideas.

Industry/Entity Type

Business

Requirements
Must have
• Must incorporate New Company Logo into the card as shown in Uploaded file.

```html
<!DOCTYPE html>
<html lang="en">
<head>
<meta charset="utf-8">
<title>Valtrion Tools – Business Card</title>
<link rel="stylesheet" href="https://fonts.googleapis.com/css2?family=Oswald:wght@300;400&display=swap">
<style>
  :root {
    --backdrop: #333436;
    --card: #ffffff;
    --brand-red: #9b1b33;
    --brand-dark: #4a1a24;
    --text-grey: #8a8a8a;
    --shadow: rgba(0, 0, 0, 0.45);
  }
  * { margin: 0; padding: 0; box-sizing: border-box; }
  html, body {
    width: 1200px;
    height: 1200px;
    overflow: hidden;
    background: var(--backdrop);
    font-family: "Oswald", "Arial Narrow", sans-serif;
  }
  .stage { position: relative; width: 1200px; height: 1200px; }

  .card {
    position: absolute;
    top: 443px;
    width: 522px;
    height: 313px;
    background: var(--card);
    box-shadow: 6px 6px 14px var(--shadow);
  }
  .card--front { left: 54px; }
  .card--back { left: 624px; }

  /* Front */
  .brand {
    position: absolute;
    left: 39px;
    top: 168px;
    display: flex;
    align-items: center;
    gap: 8px;
  }
  .brand__dot {
    width: 18px;
    height: 18px;
    border-radius: 50%;
    background: var(--brand-red);
  }
  .brand__name {
    font-weight: 300;
    font-size: 26px;
    line-height: 1;
    color: var(--brand-dark);
    letter-spacing: 0.5px;
  }
  .rule {
    position: absolute;
    left: 0;
    right: 0;
    top: 209px;
    height: 1px;
    background: var(--brand-red);
  }
  .person {
    position: absolute;
    right: 39px;
    top: 183px;
    text-align: right;
  }
  .person__name {
    font-weight: 300;
    font-size: 23px;
    line-height: 1;
    color: var(--brand-red);
  }
  .person__role {
    font-weight: 300;
    font-size: 12px;
    line-height: 1;
    margin-top: 6px;
    color: var(--text-grey);
  }
  .contact {
    position: absolute;
    left: 0;
    right: 0;
    top: 267px;
    text-align center;
    text-align: center;
    font-weight: 300;
    font-size: 15px;
    color: var(--text-grey);
    letter-spacing: 0.6px;
  }

  /* Back */
  .brand--large {
    left: 0;
    right: 0;
    top: 124px;
    justify-content: center;
    gap: 14px;
  }
  .brand--large .brand__dot { width: 46px; height: 46px; }
  .brand--large .brand__name { font-size: 40px; color: var(--brand-red); }
  .address {
    position: absolute;
    left: 0;
    right: 0;
    top: 264px;
    text-align: center;
    font-weight: 300;
    font-size: 14.5px;
    letter-spacing: 6.6px;
    color: var(--text-grey);
  }
</style>
</head>
<body>
<main class="stage">
  <section class="card card--front">
    <div class="brand">
      <span class="brand__dot"></span>
      <span class="brand__name">VALTRION TOOLS</span>
    </div>
    <div class="rule"></div>
    <div class="person">
      <p class="person__name">JOHN DOE</p>
      <p class="person__role">DIRECTOR</p>
    </div>
    <p class="contact">(065) 470218 | (065) 4702190 | john@valtriontools.com | www.valtriontools.com</p>
  </section>

  <section class="card card--back">
    <div class="brand brand--large">
      <span class="brand__dot"></span>
      <span class="brand__name">VALTRION TOOLS</span>
    </div>
    <p class="address">dummy&nbsp; dummy, dummy dummy City dummy</p>
  </section>
</main>
</body>
</html>
```